Business Cards

The name of our firm is "Tallpine Insurance adjusters"
We separate ourselves from all other public adjusters because most of us worked for the insurance companies so we understand their games.
As Insurance adjusters we represent the Insured, not the insurance companies. Our # 1 priority is to handle the entire claim process as seamless as possible on behalf of the homeowner/business owner so they don't have to deal with the hassles and headaches. Just as the logo your team designed, I want the cards to stand out from everyone elses. I also want the cards to help better understand our services and Value on hiring us and value that we can offer.
I uploaded the logo whenever I created the project. I don't see an option on re uploading the logo anywhere. Any advise??

```html
<!DOCTYPE html>
<html lang="en">
<head>
<meta charset="utf-8">
<title>Tallpine Insurance Adjusters – Business Cards</title>
<link rel="stylesheet" href="https://fonts.googleapis.com/css2?family=Josefin+Sans:wght@400;600;700&display=swap">
<style>
  :root {
    --backdrop: #c4c6c8;
    --brand-blue: #0a6fa3;
    --brand-blue-light: #0b7ab2;
    --brand-blue-dark: #075783;
    --ink: #1f2328;
    --ink-soft: #3a3f45;
    --paper: #ffffff;
  }
  * { margin: 0; padding: 0; box-sizing: border-box; }
  html, body {
    width: 1187px;
    height: 1200px;
    overflow: hidden;
    background: var(--backdrop);
    font-family: "Josefin Sans", sans-serif;
  }
  .card {
    position: absolute;
    overflow: hidden;
  }
  .card-front {
    left: 216px;
    top: 119px;
    width: 756px;
    height: 435px;
    background: linear-gradient(180deg, var(--brand-blue-light) 0%, var(--brand-blue-dark) 100%);
  }
  .card-back {
    left: 213px;
    top: 641px;
    width: 763px;
    height: 439px;
    background: var(--paper);
  }
  .wordmark {
    position: absolute;
    text-align: center;
    font-weight: 700;
    text-transform: uppercase;
    line-height: 1;
  }
  .wordmark .wordmark-name {
    display: block;
    font-size: 44px;
    letter-spacing: 1px;
  }
  .wordmark .wordmark-tagline {
    display: block;
    font-size: 13px;
    letter-spacing: 1.5px;
    margin-top: 6px;
  }
  .card-front .wordmark {
    color: var(--paper);
    left: 0;
    right: 0;
    top: 192px;
  }
  .card-back .wordmark {
    color: var(--brand-blue);
    left: 78px;
    width: 260px;
    top: 196px;
  }
  .card-back .wordmark .wordmark-name { font-size: 38px; }
  .card-back .wordmark .wordmark-tagline { font-size: 11px; }
  .divider {
    position: absolute;
    left: 379px;
    top: 124px;
    width: 2px;
    height: 192px;
    background: var(--ink);
  }
  .divider::after {
    content: "";
    position: absolute;
    left: -1px;
    top: 41px;
    width: 4px;
    height: 108px;
    background: var(--brand-blue);
  }
  .person {
    position: absolute;
    left: 422px;
    top: 117px;
  }
  .person-name {
    font-size: 30px;
    font-weight: 700;
    letter-spacing: 1.5px;
    color: var(--brand-blue);
    text-transform: uppercase;
  }
  .person-title {
    font-size: 17px;
    font-weight: 600;
    color: var(--ink-soft);
    margin-top: 6px;
    letter-spacing: 0.5px;
  }
  .contact-list {
    position: absolute;
    left: 422px;
    top: 234px;
    list-style: none;
  }
  .contact-list li {
    display: flex;
    align-items: center;
    height: 31.5px;
    font-size: 19px;
    letter-spacing: 2px;
    color: var(--ink);
  }
  .contact-list svg {
    width: 14px;
    height: 14px;
    margin-right: 10px;
    fill: var(--brand-blue);
    flex: none;
  }
  .bottom-band {
    position: absolute;
    left: 0;
    bottom: 0;
    width: 100%;
    height: 16px;
    background: linear-gradient(90deg, var(--brand-blue-dark), var(--brand-blue-light));
    border-top: 1px solid var(--ink);
  }
</style>
</head>
<body>

<section class="card card-front" aria-label="Card front">
  <div class="wordmark">
    <span class="wordmark-name">Tallpine</span>
    <span class="wordmark-tagline">Insurance Adjusters</span>
  </div>
</section>

<section class="card card-back" aria-label="Card back">
  <div class="wordmark">
    <span class="wordmark-name">Tallpine</span>
    <span class="wordmark-tagline">Insurance Adjusters</span>
  </div>

  <div class="divider"></div>

  <div class="person">
    <h1 class="person-name">Daniel Whitaker</h1>
    <p class="person-title">Founder &amp; CEO</p>
  </div>

  <ul class="contact-list">
    <li>
      <svg viewBox="0 0 24 24" aria-hidden="true"><path d="M6.6 10.8a15.1 15.1 0 0 0 6.6 6.6l2.2-2.2c.3-.3.7-.4 1-.2 1.1.4 2.3.6 3.6.6.6 0 1 .4 1 1V20c0 .6-.4 1-1 1A17 17 0 0 1 3 4c0-.6.4-1 1-1h3.5c.6 0 1 .4 1 1 0 1.3.2 2.5.6 3.6.1.3 0 .7-.2 1z"/></svg>
      321-555-0147
    </li>
    <li>
      <svg viewBox="0 0 24 24" aria-hidden="true"><path d="M2 5h20v14H2z M2 6l10 7 10-7" fill="none"/><path d="M2 5h20v2.2l-10 7-10-7zM2 9.6l10 7 10-7V19H2z"/></svg>
      info@yourwebsite.com
    </li>
    <li>
      <svg viewBox="0 0 24 24" aria-hidden="true"><circle cx="12" cy="12" r="10"/></svg>
      www.yourwebsite.com
    </li>
  </ul>

  <div class="bottom-band"></div>
</section>

</body>
</html>
```